Business card templates for our website plus designer opportunity

we require 100 business card designs to start with in the following categories (see below ) please note we require 1000`s of designs in all types of different fields this is just a tester to check the response , we are currently setting up a cardloom / printova type website/ marketplace we are now looking for freelance designers to make us some default designs to launch the site.

http://www.kelvoriq.example/

Brief about kelvoriq

we our a manufacture of a large range of products covering many industries we our currently setting up a marketplace where people can buy sell create and find personalized products and custom merchandised very much like printova and mugharbor we are now at the stage of adding content to the site for its launch we our currently looking for some core design templates in fact we need a lot of designs and we are currently looking for high quality designers to join our freelance design team .

The business cards designs

Please note all the text and data on the card can be the same so set up a default template to save yourself time all we really want is the core design front and back please , use cardloom printova mug harbor for reference or ideas please make sure they are not copied and we have full rights to the any copyright your design may contain , if we pick your designs you we will paid for them asked to make another 200 designs and you will be asked if you would like to join our freelance kelvoriq core design team you can always say no its perfectly fine but we have a lot of work to be designed for a lot of different products so there is a good opportunity here to get in before the site goes live in the next few months

Also note the chosen designs must be in vector format as well as jpeg and pdf , any vector files must be created to outlines
once we buy the designs we will own full rights to the copyright of said design and we can change and use these designs in anyway we see fit

Industry: ( 20 number designs for each ) Test run to check response

Agriculture & Farming
Animals & Pet Care
Art & Entertainment
Automotive & Transportation
Beauty & Spa

```html
<!DOCTYPE html>
<html lang="en">
<head>
<meta charset="utf-8">
<title>Kelvoriq Beauty &amp; Spa – Business Card</title>
<link rel="stylesheet" href="https://fonts.googleapis.com/css2?family=Cinzel:wght@400;500&family=Lato:wght@400;700&display=swap">
<style>
  :root {
    --page-bg: #d9d9d9;
    --card-dark: #1f1d1c;
    --card-dark-2: #2e2b29;
    --accent: #c8843c;
    --ink-light: #f2efea;
    --ink-muted: #cfc9c2;
    --frame-line: #e8e6e3;
    --photo-amber: #a8712f;
    --photo-brown: #5a3f26;
  }
  * { box-sizing: border-box; margin: 0; padding: 0; }
  html, body {
    width: 1200px; height: 900px; overflow: hidden;
    background: var(--page-bg);
  }
  .canvas { position: relative; width: 1200px; height: 900px; }
  .card {
    position: absolute; left: 270px; width: 660px; height: 377px;
    border-radius: 2px; overflow: hidden;
    box-shadow: 0 6px 18px rgba(0,0,0,.28);
    background: linear-gradient(160deg, var(--card-dark-2) 0%, var(--card-dark) 70%);
    color: var(--ink-light);
  }
  .card--back { top: 48px; }
  .card--front { top: 475px; }

  /* Back */
  .back-frame { position: absolute; inset: 0; }
  .back-company {
    position: absolute; left: 0; right: 0; top: 162px;
    text-align: center;
    font-family: "Cinzel", serif; font-size: 30px; font-weight: 400;
    letter-spacing: 1.5px; color: var(--ink-light);
  }
  .back-web {
    position: absolute; left: 0; right: 0; top: 308px;
    text-align: center;
    font-family: "Cinzel", serif; font-size: 10px; letter-spacing: 1px;
    color: var(--ink-muted);
  }

  /* Front */
  .front-photo {
    position: absolute; left: 0; top: 0; width: 440px; height: 100%;
    background: linear-gradient(180deg, var(--photo-brown) 0%, var(--photo-amber) 60%, var(--photo-brown) 100%);
    -webkit-mask-image: linear-gradient(90deg, #000 60%, transparent 100%);
            mask-image: linear-gradient(90deg, #000 60%, transparent 100%);
  }
  .front-band {
    position: absolute; left: 0; bottom: 22px; width: 400px; height: 54px;
    background: linear-gradient(90deg, rgba(255,255,255,.2), rgba(255,255,255,.08) 80%, transparent);
  }
  .brand {
    position: absolute; right: 48px; top: 42px;
    font-family: "Lato", sans-serif; text-align: right;
  }
  .brand-name {
    font-size: 27px; font-weight: 700; letter-spacing: 1px; color: var(--accent);
  }
  .brand-tagline {
    font-size: 12px; color: var(--ink-light); margin-top: -2px;
  }
  .person {
    position: absolute; right: 20px; top: 150px;
    font-family: "Lato", sans-serif; text-align: right;
  }
  .person-name { font-size: 17px; letter-spacing: .5px; white-space: nowrap; }
  .person-first { color: var(--accent); font-weight: 700; }
  .person-last { color: var(--ink-light); }
  .person-title { font-size: 9px; letter-spacing: 1px; color: var(--ink-muted); margin-top: 2px; padding-right: 52px; }

  .contact {
    position: absolute; display: flex; align-items: center; gap: 12px;
    font-family: "Lato", sans-serif; font-size: 12px; line-height: 1.3;
    color: var(--ink-light); white-space: nowrap;
  }
  .contact svg { width: 20px; height: 20px; flex: none; }
  .contact--web { left: 470px; top: 230px; }
  .contact--phone { left: 340px; top: 296px; }
  .contact--address { left: 34px; top: 310px; font-size: 13px; }
</style>
</head>
<body>
<main class="canvas">

  <section class="card card--back" aria-label="Card back">
    <svg class="back-frame" viewBox="0 0 660 377" aria-hidden="true">
      <path d="M250 300 H60 V40 H600 V270" fill="none" stroke="var(--frame-line)" stroke-width="1.5"/>
      <path d="M470 300 H600" fill="none" stroke="var(--frame-line)" stroke-width="1.5"/>
    </svg>
    <h2 class="back-company">Company Name</h2>
    <p class="back-web">www.kelvoriq.example</p>
  </section>

  <section class="card card--front" aria-label="Card front">
    <div class="front-photo" role="img" aria-label="Photo area: warm spa still life with candle, oil bottles and a rolled towel"></div>
    <div class="front-band"></div>

    <div class="brand">
      <div class="brand-name">KELVORIQ</div>
      <div class="brand-tagline">Beauty &amp; Spa</div>
    </div>

    <div class="person">
      <div class="person-name"><span class="person-first">MARCUS</span> <span class="person-last">ELLERY</span></div>
      <div class="person-title">PRESIDENT</div>
    </div>

    <div class="contact contact--web">
      <svg viewBox="0 0 20 20" aria-hidden="true">
        <g fill="none" stroke="var(--ink-light)" stroke-width="1.3">
          <circle cx="10" cy="10" r="8.5"/>
          <ellipse cx="10" cy="10" rx="3.8" ry="8.5"/>
          <path d="M1.5 10 H18.5 M3 5.5 H17 M3 14.5 H17"/>
        </g>
      </svg>
      <div>contact@kelvoriq.example<br>www.kelvoriq.example</div>
    </div>

    <div class="contact contact--phone">
      <svg viewBox="0 0 20 20" aria-hidden="true">
        <path fill="var(--ink-light)" d="M5 2.5 l3 3.2 -1.6 2 c1 2 2.6 3.6 4.6 4.6 l2-1.6 3.2 3 -1.8 2.6 C9 16 4 11 2.5 4.3 Z"/>
      </svg>
      <div>555 010 4421<br>555 010 7780</div>
    </div>

    <div class="contact contact--address">
      <svg viewBox="0 0 20 20" aria-hidden="true">
        <path fill="var(--ink-light)" d="M10 2 L19 10 H16 V18 H12 V13 H8 V18 H4 V10 H1 Z"/>
      </svg>
      <div>48 Harlow Lane<br>Brenford, IL 60999</div>
    </div>
  </section>

</main>
</body>
</html>
```